Card for modern wood artisan that builds log homes and timber frames.

Design a card with catchy imagery. With a quick list of things I build and services I offer.

I'd like an English side and a french side. I can provide the text.

I am basically a guy that builds log homes and timber frames , but I am very eco friendly oriented.

I use only eco friendly products to limit my carbon footprint.
I want the client to feel as if they are hiring a good smart builder.

I have been building for a while but just starting out to market myself out there , not just work for other companies. Starting
My own thing legitimately.

I am very conscientious, and I take care of the work I do. I am trying to bring a new age, modern feel to an old profession.

Reason: I am not completely satisfied with A model yet, looking for that masculin rustic artistic design that I havent completely found yet. Thank you for your sumbissions.

Target Market(s)

People looking to hire a builder to design and build their projects.
And contractors that want to hire a quality subcontractor for their jobs.

Industry/Entity Type

Construction

Contact Information for Business Card

I want my logo on it, that I had designed here.
And a list of services I provide.

With my phone number, website adress and Email.

Requirements
Must have
• Artful presentation,
• Eco friendly feel
• I love trees.

```html
<!DOCTYPE html>
<html lang="en">
<head>
<meta charset="utf-8">
<title>Hollinwood – Business Card</title>
<link rel="stylesheet" href="https://fonts.googleapis.com/css2?family=Saira+Semi+Condensed:wght@400;600;700&display=swap">
<style>
  :root {
    --backdrop: #101010;
    --card: #ffffff;
    --gold: #d1922a;
    --ink: #111111;
    --tree-light: #e0ad55;
    --tree-dark: #c4861f;
  }
  * { margin: 0; padding: 0; box-sizing: border-box; }
  html, body {
    width: 1200px; height: 1000px; overflow: hidden;
    background: var(--backdrop);
    font-family: "Saira Semi Condensed", sans-serif;
  }
  .business-card {
    position: absolute; left: 180px; top: 260px;
    width: 840px; height: 480px;
    background: var(--card);
    border-radius: 38px;
    overflow: hidden;
    box-shadow: 0 18px 40px rgba(0,0,0,.55);
  }
  .card-art { position: absolute; inset: 0; width: 840px; height: 480px; z-index: 1; }
  .tree-illustration {
    position: absolute; left: 150px; top: 45px;
    width: 170px; height: 262px;
    border-radius: 50% 50% 20% 20% / 70% 70% 10% 10%;
    background: linear-gradient(180deg, var(--tree-light), var(--tree-dark));
    z-index: 0;
  }
  .brand {
    position: absolute; left: 92px; top: 145px; z-index: 2;
    display: flex; align-items: center; gap: 10px;
    background: var(--card);
    border: 4px solid var(--ink);
    padding: 6px 16px 6px 10px;
  }
  .brand-mark { width: 26px; height: 26px; background: var(--ink); }
  .brand-name { font-size: 34px; font-weight: 700; color: var(--ink); letter-spacing: 1px; line-height: 1; }
  .owner { position: absolute; left: 450px; top: 110px; color: var(--ink); z-index: 2; }
  .owner-name { font-size: 30px; font-weight: 700; line-height: 1; }
  .owner-role { font-size: 22px; font-weight: 400; margin-top: 4px; }
  .contact-list { position: absolute; left: 420px; top: 188px; list-style: none; z-index: 2; }
  .contact-item {
    display: flex; align-items: center; gap: 16px;
    height: 42px; font-size: 22px; font-weight: 600; color: var(--ink);
  }
  .contact-icon {
    width: 32px; height: 32px; border-radius: 50%;
    background: var(--gold);
    display: flex; align-items: center; justify-content: center;
  }
  .services-text { font-size: 21px; font-weight: 400; fill: var(--ink); }
</style>
</head>
<body>
  <article class="business-card">
    <div class="tree-illustration" role="img" aria-label="Sketched golden pine tree with roots standing on the hill"></div>

    <svg class="card-art" viewBox="0 0 840 480" aria-hidden="true">
      <defs>
        <path id="services-curve" d="M25,345 C230,335 430,385 570,430 C660,458 740,462 810,450"/>
      </defs>
      <path class="gold-wave" fill="var(--gold)"
            d="M0,300 C200,285 420,330 560,395 C680,450 770,440 840,415 L840,480 L0,480 Z"/>
      <text class="services-text">
        <textPath href="#services-curve" textLength="770" lengthAdjust="spacingAndGlyphs">First Service | Second Service | Third Service | Fourth Service | Fifth Service</textPath>
      </text>
    </svg>

    <div class="brand">
      <span class="brand-mark"></span>
      <span class="brand-name">HOLLINWOOD</span>
    </div>

    <div class="owner">
      <p class="owner-name">LOREM IPSUM</p>
      <p class="owner-role">Owner</p>
    </div>

    <ul class="contact-list">
      <li class="contact-item">
        <span class="contact-icon">
          <svg width="17" height="17" viewBox="0 0 24 24"><path fill="#111" d="M6.6 10.8a15 15 0 0 0 6.6 6.6l2.2-2.2c.3-.3.7-.4 1-.2 1.1.4 2.3.6 3.6.6.6 0 1 .4 1 1V20c0 .6-.4 1-1 1A17 17 0 0 1 3 4c0-.6.4-1 1-1h3.5c.6 0 1 .4 1 1 0 1.3.2 2.5.6 3.6.1.3 0 .7-.2 1z"/></svg>
        </span>
        012 345 6789
      </li>
      <li class="contact-item">
        <span class="contact-icon">
          <svg width="17" height="17" viewBox="0 0 24 24"><path fill="#111" d="M3 5h18v14H3z"/><path fill="none" stroke="#d1922a" stroke-width="1.8" d="M3 6l9 7 9-7"/></svg>
        </span>
        youremail@domain.com
      </li>
      <li class="contact-item">
        <span class="contact-icon">
          <svg width="17" height="17" viewBox="0 0 24 24" fill="none" stroke="#111" stroke-width="1.8"><circle cx="12" cy="12" r="9"/><ellipse cx="12" cy="12" rx="4" ry="9"/><path d="M3 12h18M5 7h14M5 17h14"/></svg>
        </span>
        www.yourwebsite.com
      </li>
    </ul>
  </article>
</body>
</html>
```